Morrow Engineering Core Values Branding Package

Morrow Engineering has recently refined its company Core Values and is seeking a strong, cohesive branding package to visually bring these values to life. The new graphic assets will communicate our commitment to excellence in a way that resonates with our team, clients, and partners in a blue-collar, industrial environment.

We are looking for multiple visual assets with consistent design elements that can be applied across platforms. The tone should reflect strength, reliability, and professionalism while remaining approachable and aligned with our industry.

Core Values & Descriptions
Accountability
“We take ownership of our work and actions, ensuring reliability and trust in every solution we deliver.”

Teamwork
“We collaborate across departments and disciplines to provide the highest level of service and innovation for our clients.”

Integrity
“We operate with honesty, transparency, and ethical standards in all aspects of our business.”

Growth
“We are committed to continuous improvement—of our people, our processes, and our impact in the industry.”

Deliverables

1. Primary Core Values Graphic
A master visual representing all four values together.
Designed for use on posters, office signage, internal presentations.

2. Individual Value Graphics (x4)
One graphic per core value: Accountability, Teamwork, Integrity, Growth.
Cohesive style with slight visual variation to reflect each value’s unique meaning.

Target Market(s)

Employees of Morrow Engineering

Industry/Entity Type

Blue Collar

Font styles to use
Sans Serif

Colors
0054AA
0677BA
7BADD7
CADEEF
E8F1F8
00AB8E
00BBA5
67D7C9
C6EFE9
E9F9F6
EB3D1F
EC4F4E
F09395
F8D3D4
FCEDEE

Requirements
Must have
• Accountability, Teamwork, Integrity, Growth

```html
<!DOCTYPE html>
<html lang="en">
<head>
<meta charset="utf-8">
<title>Morrow Engineering – Core Values</title>
<link href="https://fonts.googleapis.com/css2?family=Archivo:wght@700;800&family=Roboto+Condensed:wght@400;700&display=swap" rel="stylesheet">
<style>
  :root {
    --navy: #0b2f6b;
    --green: #3aaa35;
    --green-soft: #eef7ec;
    --grey-soft: #eff0f4;
    --icon-fill: #dfe4ee;
    --ink: #2b2b2b;
    --rule: #8a8a8a;
    --page: #ececec;
    --white: #ffffff;
  }
  html, body { margin: 0; padding: 0; overflow: hidden; }
  body {
    width: 1200px; height: 1146px;
    background: var(--page);
    position: relative;
    font-family: "Roboto Condensed", "Arial Narrow", sans-serif;
  }
  .poster {
    position: absolute; left: 0; top: 149px;
    width: 1200px; height: 848px;
    background: var(--white);
    overflow: hidden;
  }
  .poster > * { position: absolute; }
  .backdrop { left: 0; top: 0; width: 1200px; height: 848px; }
  .brand-name {
    left: 79px; top: 92px; margin: 0;
    font-family: "Roboto Condensed", sans-serif; font-weight: 700;
    font-size: 56px; letter-spacing: 1px; color: var(--navy);
  }
  .title {
    right: 80px; top: 96px; margin: 0;
    font-family: "Archivo", sans-serif; font-weight: 800;
    font-size: 68px; line-height: 1; letter-spacing: -1px;
    color: var(--navy);
  }
  .title .accent { color: var(--green); }
  .divider { left: 75px; top: 205px; width: 1049px; height: 1px; background: var(--rule); }
  .value { width: 260px; }
  .value h3 {
    margin: 0; font-weight: 700; font-size: 31px; line-height: 1;
    color: var(--navy); letter-spacing: 0.2px;
  }
  .value .rule { height: 1px; background: var(--rule); width: 134px; margin: 9px 0 7px; }
  .value p { margin: 0; font-size: 19px; line-height: 21.5px; color: var(--ink); }
  .value.left { text-align: right; }
  .value.left .rule { margin-left: auto; }
  .value.left p { width: 222px; margin-left: auto; }
  .value.right p { width: 234px; }
  .value-accountability { left: 36px; top: 302px; }
  .value-integrity { left: 36px; top: 590px; }
  .value-teamwork { left: 870px; top: 302px; }
  .value-growth { left: 870px; top: 590px; }
  .site {
    left: 0; width: 1200px; top: 790px; margin: 0;
    text-align: center; font-size: 29px; color: var(--white);
  }
</style>
</head>
<body>
<main class="poster">
  <svg class="backdrop" viewBox="0 0 1200 848" xmlns="http://www.w3.org/2000/svg">
    <defs>
      <linearGradient id="topGreen" x1="0" x2="1">
        <stop offset="0" stop-color="#3aaa35"/>
        <stop offset="0.55" stop-color="#3aaa35"/>
        <stop offset="1" stop-color="#3aaa35" stop-opacity="0"/>
      </linearGradient>
      <radialGradient id="ringShadow" cx="0.5" cy="0.55" r="0.5">
        <stop offset="0.7" stop-color="#000" stop-opacity="0.18"/>
        <stop offset="1" stop-color="#000" stop-opacity="0"/>
      </radialGradient>
    </defs>
    <path class="swoosh-green" d="M0 260 C300 100 700 20 960 40 L1200 200 L1200 560 C1150 300 1000 130 700 80 C420 40 150 150 0 290 Z" fill="var(--green-soft)"/>
    <path class="swoosh-grey" d="M0 380 C250 260 450 220 700 210 C940 200 1130 320 1120 560 C1080 330 880 240 650 260 C420 280 180 420 20 600 L0 600 Z" fill="var(--grey-soft)"/>
    <rect x="0" y="0" width="380" height="41" fill="url(#topGreen)"/>
    <rect x="385" y="0" width="815" height="17" fill="var(--navy)"/>
    <polygon points="388,0 500,0 482,41 372,41" fill="var(--navy)"/>
    <circle cx="590" cy="480" r="155" fill="none" stroke="var(--green)" stroke-width="25"/>
    <g class="badge badge-accountability">
      <circle cx="440" cy="348" r="112" fill="url(#ringShadow)"/>
      <circle cx="436" cy="341" r="108" fill="var(--white)"/>
      <circle cx="436" cy="341" r="94" fill="var(--navy)"/>
      <circle cx="436" cy="341" r="74" fill="var(--white)"/>
      <circle cx="436" cy="341" r="44" fill="var(--icon-fill)" role="img" aria-label="Icon: open hand holding a shield"/>
    </g>
    <g class="badge badge-teamwork">
      <circle cx="747" cy="348" r="112" fill="url(#ringShadow)"/>
      <circle cx="743" cy="341" r="108" fill="var(--white)"/>
      <circle cx="743" cy="341" r="94" fill="var(--navy)"/>
      <circle cx="743" cy="341" r="74" fill="var(--white)"/>
      <circle cx="743" cy="341" r="44" fill="var(--icon-fill)" role="img" aria-label="Icon: two hands joining puzzle pieces"/>
    </g>
    <g class="badge badge-integrity">
      <circle cx="440" cy="625" r="112" fill="url(#ringShadow)"/>
      <circle cx="436" cy="618" r="108" fill="var(--white)"/>
      <circle cx="436" cy="618" r="94" fill="var(--navy)"/>
      <circle cx="436" cy="618" r="74" fill="var(--white)"/>
      <circle cx="436" cy="618" r="44" fill="var(--icon-fill)" role="img" aria-label="Icon: handshake beneath a shield"/>
    </g>
    <g class="badge badge-growth">
      <circle cx="747" cy="625" r="112" fill="url(#ringShadow)"/>
      <circle cx="743" cy="618" r="108" fill="var(--white)"/>
      <circle cx="743" cy="618" r="94" fill="var(--navy)"/>
      <circle cx="743" cy="618" r="74" fill="var(--white)"/>
      <circle cx="743" cy="618" r="44" fill="var(--icon-fill)" role="img" aria-label="Icon: rising bars with an upward arrow"/>
    </g>
    <polygon points="0,823 390,823 382,845 0,845" fill="var(--green)"/>
    <polygon points="810,823 1200,823 1200,845 818,845" fill="var(--green)"/>
    <polygon points="418,780 770,780 795,848 398,848" fill="var(--navy)"/>
  </svg>

  <h1 class="brand-name">MORROW</h1>
  <h2 class="title">Core <span class="accent">Values</span></h2>
  <div class="divider"></div>

  <section class="value left value-accountability">
    <h3>ACCOUNTABILITY</h3>
    <div class="rule"></div>
    <p>We take ownership of our work and actions, ensuring reliability and trust in every solution we deliver.</p>
  </section>
  <section class="value right value-teamwork">
    <h3>TEAMWORK</h3>
    <div class="rule"></div>
    <p>We collaborate across departments and disciplines to provide the highest level of service and innovation for our clients.</p>
  </section>
  <section class="value left value-integrity">
    <h3>INTEGRITY</h3>
    <div class="rule"></div>
    <p>We operate with honesty, transparency, and ethical standards in all aspects of our business.</p>
  </section>
  <section class="value right value-growth">
    <h3>GROWTH</h3>
    <div class="rule"></div>
    <p>We are committed to continuous improvement—of our people, our processes, and our impact in the industry.</p>
  </section>

  <p class="site">www.morrowengineering.com</p>
</main>
</body>
</html>
```